Flyer Design Project

We need a flyer (in Spanish) for:
"Feria Mezcal & Oficios Valle Dorado 2013"
This event will be held in Los Angeles CA and would like to attract exhibitors.
Must include the information provided in the word file.

Target Market(s)

Tequila producers and distributors

Industry/Entity Type

Event

Requirements
Must have
• pictures to be used at your discretion

```html
<!DOCTYPE html>
<html lang="es">
<head>
<meta charset="utf-8">
<title>Feria Mezcal &amp; Oficios Valle Dorado 2013</title>
<link href="https://fonts.googleapis.com/css2?family=UnifrakturMaguntia&family=Questrial&family=Arimo:wght@400;700&display=swap" rel="stylesheet">
<style>
  :root {
    --wood-dark: #1e1512;
    --wood-mid: #3a2c26;
    --wood-light: #5a4840;
    --panel-top: #c9cdcf;
    --panel-bottom: #f1f2f2;
    --ink: #161616;
    --oval: #151515;
    --white: #ffffff;
  }
  * { margin: 0; padding: 0; box-sizing: border-box; }
  html, body { width: 856px; height: 1200px; overflow: hidden; background: var(--wood-dark); }
  .flyer {
    position: relative; width: 856px; height: 1200px; overflow: hidden;
    background:
      repeating-linear-gradient(90deg, transparent 0 9px, rgba(255,255,255,0.05) 9px 11px, transparent 11px 23px, rgba(0,0,0,0.25) 23px 26px),
      linear-gradient(90deg, var(--wood-dark), var(--wood-mid) 30%, var(--wood-dark) 55%, var(--wood-light) 80%, var(--wood-dark));
  }
  .title {
    position: absolute; top: 50px; left: 0; width: 856px; text-align: center;
    font-family: "UnifrakturMaguntia", serif; font-size: 42px; font-weight: 400; color: var(--white);
    line-height: 1; white-space: nowrap;
  }
  .tagline {
    position: absolute; top: 98px; left: 0; width: 856px; text-align: center;
    font-family: "Arimo", sans-serif; font-weight: 700; font-size: 14px; color: var(--white);
  }
  .info-panel {
    position: absolute; left: 0; top: 185px; width: 542px; height: 650px;
    background: linear-gradient(180deg, var(--panel-top), var(--panel-bottom) 70%, #fafafa);
  }
  .intro {
    position: absolute; left: 58px; top: 222px; width: 472px;
    font-family: "Questrial", sans-serif; font-size: 13.6px; line-height: 19.5px; color: var(--ink);
    text-align: justify;
  }
  .intro p { text-indent: 48px; margin-bottom: 18px; }
  .intro p:last-child { margin-bottom: 0; }
  .date-oval {
    position: absolute; left: 12px; top: 630px; width: 510px; height: 170px; border-radius: 50%;
    background: var(--oval); color: var(--white); text-align: center;
    font-family: "Arimo", sans-serif;
  }
  .date-oval .lead { margin-top: 12px; font-size: 21px; line-height: 29px; word-spacing: 5px; }
  .date-oval .details { margin: 8px auto 0; width: 410px; font-size: 12.2px; line-height: 16px; }
  .photo { position: absolute; }
  .photo-agave { left: 542px; top: 190px; width: 314px; height: 205px; background: linear-gradient(180deg, #c9d4dc 0%, #a7b49a 28%, #3f5436 55%, #2a3a2a 100%); }
  .photo-barrels { left: 542px; top: 400px; width: 314px; height: 224px; background: linear-gradient(90deg, #5b3f2c, #a98a6a 35%, #e7e2dc 55%, #6a4c34 85%, #3c291c); }
  .photo-pottery { left: 542px; top: 626px; width: 314px; height: 205px; background: linear-gradient(90deg, #7a8a3c, #d47a2c 30%, #b9522a 60%, #c7d4e2); }
  .photo-guests { left: 0; top: 835px; width: 496px; height: 365px; background: linear-gradient(180deg, #e6e6e6 0%, #caa890 35%, #7a5238 70%, #3c2a22 100%); }
  .torn { position: absolute; left: 0; width: 856px; }
  .torn-top { top: 150px; height: 60px; }
  .torn-bottom { top: 808px; height: 45px; }
  .contact {
    position: absolute; left: 524px; top: 960px; width: 320px; color: var(--white);
    font-family: "Arimo", sans-serif;
  }
  .contact .call { font-size: 11px; font-weight: 700; margin-left: 22px; }
  .contact .cols { display: flex; margin-top: 36px; }
  .contact .col { width: 168px; }
  .contact .region { font-size: 14px; line-height: 16px; }
  .contact .name { font-size: 11.5px; line-height: 15px; }
  .contact .phone { font-size: 17px; font-weight: 700; line-height: 24px; }
  .contact .email { font-size: 11px; line-height: 15px; }
  .contact .web { margin-top: 26px; font-size: 11px; font-weight: 700; text-align: center; width: 310px; }
</style>
</head>
<body>
<main class="flyer">
  <h1 class="title">Feria Mezcal &amp; Oficios Valle Dorado 2013</h1>
  <p class="tagline">¡Vinculando marcas emergentes e innovadoras en una época de descubrimiento de sabores mundiales!</p>

  <div class="info-panel"></div>
  <div class="photo photo-agave" role="img" aria-label="Jimador cosechando agave en un campo de agaves azules"></div>
  <div class="photo photo-barrels" role="img" aria-label="Dos hombres catando tequila entre barricas de roble"></div>
  <div class="photo photo-pottery" role="img" aria-label="Vasijas de barro artesanales pintadas"></div>

  <svg class="torn torn-top" viewBox="0 0 856 60" preserveAspectRatio="none" aria-hidden="true">
    <path d="M0 30 L40 28 L70 36 L110 26 L150 33 L185 29 L215 40 L240 24 L262 38 L300 31 L340 37 L380 30 L420 41 L455 33 L490 38 L520 30 L540 50 L545 60 L0 60 Z" fill="#c9cdcf"/>
    <path d="M0 24 L40 22 L70 31 L110 20 L150 27 L185 23 L215 34 L240 10 L262 32 L300 25 L340 31 L380 24 L420 35 L455 27 L470 4 L490 32 L520 24 L560 36 L600 30 L640 38 L680 28 L720 36 L760 30 L800 38 L830 32 L856 36 L856 44 L800 44 L720 42 L640 44 L560 44 L540 46 L520 38 L480 42 L420 44 L340 40 L240 42 L150 38 L70 42 L0 36 Z" fill="#ffffff"/>
  </svg>

  <div class="intro">
    <p>Chile, España, Escocia, Francia, Argentina, Polonia, Mexico – cuando buscamos que beber, buscamos en el mundo, y ese mundo termina en nuestros vasos. Queremos lo mejor, lo más sabroso, lo interesante y estamos dispuestos a recorrer grandes distancias para obtenerlo.</p>
    <p>La promoción y la creatividad son, quizás, aún más importante en tiempos de incertidumbre económica, cuando se es implacable en la búsqueda de nuevos clientes. Con unas perspectivas más amplias, más globales, ya sea sondeando tradiciones centenarias, o la exploración de las fronteras de las bebidas de moda, buscando nuevas mercados, o re-inventando su marca para mantenerse competitivos.</p>
    <p>En esta edición especializada en Tequila, vamos a discutir las técnicas, procesos creativos, perfiles de sabor, tecnologías, y los ingredientes que son cada vez más esenciales de la caja de herramientas del Coctelero (Mixologist) del siglo 21.</p>
    <p>Tendremos una competencia de las cuatro variedades de tequila: Blanco, Reposado, Añejo y Extra Añejo; con reconocimiento a los ganadores de cada categoría.</p>
  </div>

  <div class="date-oval">
    <p class="lead">Acompáñanos, los días<br>29 y 30 de agosto 2013, Los Angeles,</p>
    <p class="details">donde se vincularan, consumidores, bares, detallistas, restaurantes y distribuidores, en la matriz de creatividad coctelera, talento culinario, sabores de moda y uno de los mercados más importantes e influyentes del mundo.</p>
  </div>

  <div class="photo photo-guests" role="img" aria-label="Grupo de amigos sonrientes brindando con caballitos de tequila"></div>

  <svg class="torn torn-bottom" viewBox="0 0 856 45" preserveAspectRatio="none" aria-hidden="true">
    <path d="M0 22 L30 18 L60 26 L100 16 L140 24 L180 18 L210 28 L250 20 L290 26 L330 18 L370 27 L410 20 L450 28 L470 8 L495 30 L520 22 L560 30 L600 20 L640 28 L680 18 L720 27 L760 20 L800 28 L830 14 L856 22 L856 32 L800 34 L720 32 L640 35 L560 33 L496 36 L400 32 L300 35 L200 31 L100 34 L0 30 Z" fill="#ffffff"/>
  </svg>

  <div class="contact">
    <p class="call">Para oportunidades de patrocinio y exhibición:</p>
    <div class="cols">
      <div class="col">
        <p class="region">(USA)</p>
        <p class="name">Rodrigo E. Salcedo Director</p>
        <p class="phone">+ 818-555-0142</p>
        <p class="email">rsalcedo@feriavd.com</p>
      </div>
      <div class="col">
        <p class="region">(Mexico)</p>
        <p class="name">Ing. Julián R. Ortega</p>
        <p class="phone">333-555-0187</p>
        <p class="email">jortega@feriavd.com</p>
      </div>
    </div>
    <p class="web">www.feriavd.com</p>
  </div>
</main>
</body>
</html>
```